Small rum distillery looking for bottle design

Small rum distillery in Estonia. Looking for bottle lable design. It should be simple but at the same time point out from the variety of other bottles.
As we are a small nordic country, design can be some how nordic or represent our country. It can also have some connection with sailing or sea as we know it pirates love it.
Bottle we are using is Corvane 540

Industry/Entity Type

food and beverage

Other font styles liked:
• Baskerville

```html
<!DOCTYPE html>
<html lang="en">
<head>
<meta charset="utf-8">
<title>Kaldre Distillery – Rum Label</title>
<link rel="stylesheet" href="https://fonts.googleapis.com/css2?family=EB+Garamond:wght@400;500&display=swap">
<style>
  :root {
    --page: #ffffff;
    --label: #3d3d3d;
    --ink: #f2efe4;
    --art-deep: #4a4a48;
    --art-light: #8a877e;
  }
  html, body {
    margin: 0;
    padding: 0;
    width: 1200px;
    height: 1200px;
    overflow: hidden;
    background: var(--page);
  }
  .canvas {
    position: relative;
    width: 1200px;
    height: 1200px;
  }
  .label-shape {
    position: absolute;
    left: 0;
    top: 0;
    width: 1200px;
    height: 1200px;
  }
  .label-shape .body,
  .label-shape .band {
    fill: var(--label);
  }
  .mark {
    position: absolute;
    left: 550px;
    top: 285px;
    width: 100px;
    height: 100px;
    border-radius: 50%;
    background: var(--ink);
  }
  .brand-name {
    position: absolute;
    left: 0;
    width: 1200px;
    top: 400px;
    margin: 0;
    text-align: center;
    font-family: "EB Garamond", Garamond, serif;
    font-weight: 500;
    font-size: 104px;
    line-height: 1;
    letter-spacing: 2px;
    color: var(--ink);
  }
  .brand-rule {
    position: absolute;
    left: 375px;
    top: 538px;
    width: 450px;
    height: 3px;
    background: var(--ink);
  }
  .brand-sub {
    position: absolute;
    left: 0;
    width: 1200px;
    top: 560px;
    margin: 0;
    text-align: center;
    font-family: "EB Garamond", Garamond, serif;
    font-weight: 500;
    font-size: 32px;
    line-height: 1;
    letter-spacing: 9px;
    color: var(--ink);
  }
  .illustration {
    position: absolute;
    left: 415px;
    top: 640px;
    width: 370px;
    height: 295px;
    border-radius: 12px;
    background: radial-gradient(ellipse at 55% 50%, var(--art-light) 0%, var(--art-deep) 75%);
  }
</style>
</head>
<body>
  <main class="canvas">
    <svg class="label-shape" viewBox="0 0 1200 1200" aria-hidden="true">
      <rect class="band" x="140" y="312" width="920" height="578"/>
      <rect class="body" x="220" y="215" width="760" height="770" rx="42" ry="42"/>
    </svg>
    <div class="mark" aria-hidden="true"></div>
    <h1 class="brand-name">KALDRE</h1>
    <div class="brand-rule" aria-hidden="true"></div>
    <p class="brand-sub">DISTILLERY</p>
    <div class="illustration" role="img" aria-label="Cream line illustration of a woman in profile with long hair streaming in the wind like sea waves"></div>
  </main>
</body>
</html>
```